Wine Label Design

Organization name: Halvern Wine Company

My company is called Halvern Wine Company, I’m a wine importer and wholesaler who distributes wine domestically.

We are about to launch a line of three premium and one sparkling wine that we will wholesale to various retailers, wine stores, and restaurants for re-sale. The wines label will have “Dorian Halvern” I plan on having the labels the same and just changing the varietal as needed. My wine are made from premium grapes and will be marketed as a high end wine. My current label size is 3 1/2" wide by 5" in long and the labels can be on a solid background or transparent.

I would like the first label to be for my Cabernet Sauvignon, California, 2012, 750ML (for the size of the bottle) and ALC 13.8% BY VOL (for the alcohol content).

Colors: I am open to any and all designs that would alter my perception of what will be best!

Further:
Current label is boring and poorly done, so hopefully you designers can come up with something better

Industry/Entity Type

It Company

```html
<!DOCTYPE html>
<html lang="en">
<head>
<meta charset="utf-8">
<title>Dorian Halvern – Cabernet Sauvignon Label</title>
<link rel="stylesheet" href="https://fonts.googleapis.com/css2?family=Kaushan+Script&family=Petit+Formal+Script&family=Tinos:ital,wght@0,400;1,400;1,700&display=swap">
<style>
  :root {
    --page-bg: #ffffff;
    --label-bg: #ffffff;
    --label-shadow: #8c8c8c;
    --ink-dark: #1c1c28;
    --ink-navy: #3c3d68;
    --ink-slate: #4b4c66;
    --ink-faint: #c9c9d4;
    --wash-light: #ececf3;
    --wash-mid: #c7c8da;
    --wash-deep: #6f71a0;
    --wash-dark: #545784;
    --strip: #9fa1c0;
    --band: #a9abc6;
  }
  * { margin: 0; padding: 0; box-sizing: border-box; }
  html, body {
    width: 1200px;
    height: 1000px;
    overflow: hidden;
    background: var(--page-bg);
  }
  .canvas {
    position: relative;
    width: 1200px;
    height: 1000px;
  }
  .wine-label {
    position: absolute;
    left: 300px;
    top: 8px;
    width: 595px;
    height: 975px;
    background: var(--label-bg);
    box-shadow: 8px 8px 0 var(--label-shadow);
    overflow: hidden;
  }
  .brand-name {
    position: absolute;
    left: 50px;
    right: 5px;
    top: 0;
    text-align: center;
    font-family: "Kaushan Script", cursive;
    font-size: 80px;
    font-weight: 400;
    line-height: 100px;
    color: var(--ink-dark);
    white-space: nowrap;
  }
  .artwork {
    position: absolute;
    left: 57px;
    top: 100px;
    width: 540px;
    height: 692px;
  }
  .artwork svg { display: block; }
  .region {
    position: absolute;
    left: 75px;
    top: 712px;
    font-family: "Kaushan Script", cursive;
    font-size: 53px;
    letter-spacing: 1px;
    color: var(--ink-dark);
  }
  .vintage {
    position: absolute;
    right: 22px;
    top: 702px;
    text-align: center;
    font-family: "Petit Formal Script", cursive;
    font-size: 31px;
    line-height: 38px;
    color: var(--ink-slate);
  }
  .tagline {
    position: absolute;
    left: 14px;
    top: 795px;
    transform: rotate(-90deg);
    transform-origin: 0 0;
    width: 700px;
    font-family: "Tinos", serif;
    font-style: italic;
    font-size: 40px;
    letter-spacing: 4px;
    line-height: 42px;
    color: var(--ink-faint);
    white-space: nowrap;
  }
  .tagline strong { color: var(--ink-slate); font-weight: 700; }
  .varietal {
    position: absolute;
    left: 50px;
    right: 10px;
    top: 830px;
    text-align: center;
    font-family: "Petit Formal Script", cursive;
    font-size: 46px;
    color: var(--ink-navy);
    white-space: nowrap;
  }
  .volume, .alcohol {
    position: absolute;
    top: 938px;
    font-family: "Tinos", serif;
    font-size: 21px;
    color: var(--ink-dark);
  }
  .volume { left: 15px; }
  .alcohol { right: 5px; }
</style>
</head>
<body>
<main class="canvas">
  <section class="wine-label">
    <h1 class="brand-name">Dorian Halvern</h1>

    <div class="artwork">
      <svg width="540" height="692" viewBox="0 0 540 692">
        <defs>
          <linearGradient id="washGradient" x1="0" y1="0" x2="0.7" y2="1">
            <stop offset="0" stop-color="var(--wash-light)"/>
            <stop offset="0.35" stop-color="var(--wash-mid)"/>
            <stop offset="0.6" stop-color="var(--wash-deep)"/>
            <stop offset="0.85" stop-color="var(--wash-mid)"/>
            <stop offset="1" stop-color="var(--wash-dark)"/>
          </linearGradient>
        </defs>
        <rect class="wash" x="0" y="0" width="400" height="587" fill="url(#washGradient)" role="img" aria-label="Abstract watercolour wash in lavender and indigo tones"/>
        <rect class="side-strip" x="400" y="0" width="140" height="587" fill="var(--strip)"/>
        <rect class="base-band" x="0" y="587" width="540" height="105" fill="var(--band)"/>
      </svg>
    </div>

    <p class="region">CALIFORNIA</p>
    <p class="vintage">Vintage<br>2012</p>

    <p class="tagline"><strong>wine</strong> made from premium grapes</p>

    <p class="varietal">Cabernet&nbsp; Sauvignon</p>

    <p class="volume">750ML</p>
    <p class="alcohol">ALC 13,8%</p>
  </section>
</main>
</body>
</html>
```